Etiketten-Design für eingekochte Erzeugnisse
Zielgruppe
Wir sind ein regional tätiger Cateringbetrieb und Hersteller von hausgemachten, qualitativ hochwertigen Saucen, Suppen und Dips. Für unsere eingekochten Erzeugnisse suchen wir ein Etikett für durchsichtige Gläser (327 ml, TO 66) mit kupferfarbenem Twist-Off-Deep Verschluss. Da es sich um hochwertige Produkte handelt, sollte dies auch das Etikett widerspiegeln und nicht „billig“ aussehen. Das Design sollte modern, hip und farblich zum Kupferdeckel passen.
Aufgabenstellung
Das Etikett sollte über den gesamten Umfang des Glases gehen. Als Endformat stellen wir uns eine Breite des Etiketts von 220 mm und eine Höhe von 90 mm vor.
Da wir unterschiedliche Sorten anbieten, sollten sich diese in den Etiketten wiederfinden. Jede Sorte sollte also ein individuell auf den Inhalt angepasstes Etikett haben. Zudem sollte das Etikett später auch anpassbar sein, da sich die Vorschriften zur Deklaration sowie die Zutatenliste ändern können. Die Grammangabe der Gesamtmenge sollte ebenfalls anpassbar sein können.
Für unsere Marke „Topfzauber“ suchen wir außerdem ein neues Wort-Bild-Logo,
welches gleich auf dem Etikett platziert werden soll. Das Logo sollte also in das Etikett eingefügt sein, aber auch für die Homepage und den Rechnungsbogen geeignet sein.
Unser Sortiment umfasst die Saucensorten:
- Tomatensauce
- Bratensauce
- Rahmsauce
- Bolognesesauce
- Chilli con Carne
- Linsenbolognese, vegetarisch
- Gelbes Thai Curry, vegetarisch
- Ungarische Gulaschsuppe
- Karibischer Süßkartoffel-Kürbis Eintopf
- Indischer Linsencurry
Was soll auf das Etikett:
Saucen Sorte (Bezeichnung)
Hersteller:
Partyservice Wendlinger
Matthias Wendlinger
Lindauer Gasse 7
88512 Ostrach
Inhalt:
360g
Zutaten:
Anpassbares Zutatentextfeld
Anpassbare Nährwerttabelle mit den Big 7
Haltbarkeit:
Mindestens haltbar bis: siehe Deckel
Hinweise:
Kann Spuren von Sellerie und Nüssen enthalten.
Kühl, trocken und lichtgeschützt lagern.
Nach dem Öffnen im Kühlschrank aufbewahren und innerhalb weniger Tage aufbrauchen.
Weiße Fläche freihalten, um später eventuell einen Barcode einzufügen.
Internetadresse:
www.topfzauber-beispiel.de

```html
<!DOCTYPE html>
<html lang="de">
<head>
<meta charset="utf-8">
<title>Topfzauber – Etiketten</title>
<link rel="stylesheet" href="https://fonts.googleapis.com/css2?family=Oswald:wght@500;600&family=Source+Sans+3:wght@400;700&display=swap">
<style>
  :root {
    --ink: #111111;
    --paper: #ffffff;
    --tomato: #e8525b;
    --tomato-deep: #c9424a;
    --bolognese: #ef735a;
    --bolognese-deep: #d35d46;
    --accent-red: #e8525b;
    --display: "Oswald", sans-serif;
    --text: "Source Sans 3", sans-serif;
  }
  * { box-sizing: border-box; margin: 0; padding: 0; }
  html, body { width: 900px; height: 1200px; overflow: hidden; background: var(--paper); }
  .canvas { position: relative; width: 900px; height: 1200px; background: var(--paper); font-family: var(--text); color: var(--ink); }

  /* Lid tag */
  .lid-tag { position: absolute; left: 269px; top: 0; width: 212px; height: 494px; }
  .lid-tag__disc { position: absolute; left: 0; top: 0; width: 212px; height: 212px; border-radius: 50%; background: var(--ink); }
  .lid-tag__strip { position: absolute; left: 71px; top: 180px; width: 70px; height: 314px; background: var(--ink); border-bottom: 10px solid var(--accent-red); }
  .lid-tag__claim { position: absolute; left: 120px; top: 480px; transform-origin: left top; transform: rotate(-90deg); color: var(--paper); font-family: var(--display); font-weight: 500; font-size: 11px; letter-spacing: 1px; white-space: nowrap; }
  .brand-name { font-family: var(--display); font-weight: 600; color: var(--paper); text-align: center; line-height: 1.05; letter-spacing: 0.5px; }
  .lid-tag .brand-name { position: absolute; left: 0; right: 0; top: 66px; font-size: 38px; }

  /* Jar label */
  .jar-label { position: absolute; left: 66px; width: 780px; height: 309px; border-bottom: 10px solid var(--ink); box-sizing: content-box; }
  .jar-label--tomato { top: 516px; background: var(--tomato); --deep: var(--tomato-deep); }
  .jar-label--bolognese { top: 861px; background: var(--bolognese); --deep: var(--bolognese-deep); }

  .barcode-space { position: absolute; left: 34px; top: 24px; width: 48px; height: 129px; background: var(--paper); }
  .rule-vertical { position: absolute; width: 1px; background: var(--ink); }
  .rule-vertical--left { left: 90px; top: 20px; height: 272px; }
  .rule-vertical--right { left: 555px; top: 20px; height: 275px; }
  .rule-short { position: absolute; left: 34px; top: 240px; width: 48px; height: 1px; background: var(--ink); }
  .best-before { position: absolute; left: 36px; top: 236px; transform-origin: left top; transform: rotate(-90deg); font-size: 10.5px; line-height: 1.2; white-space: nowrap; }
  .best-before strong { display: block; }
  .net-weight { position: absolute; left: 50px; top: 296px; transform-origin: left top; transform: rotate(-90deg); font-family: var(--display); font-weight: 600; font-size: 25px; line-height: 1; white-space: nowrap; }

  .herb-illustration { position: absolute; left: 178px; top: 21px; width: 268px; height: 238px; border-radius: 50%; background: radial-gradient(circle, var(--deep) 0%, var(--deep) 45%, transparent 72%); }
  .brand-disc { position: absolute; left: 221px; top: 27px; width: 176px; height: 176px; border-radius: 50%; background: var(--ink); display: flex; align-items: center; justify-content: center; }
  .brand-disc .brand-name { font-size: 33px; }
  .diet-stamp { position: absolute; left: 446px; top: 202px; width: 28px; height: 44px; border: 1px solid var(--ink); opacity: 0.7; }
  .product-name { position: absolute; left: 140px; width: 340px; top: 242px; text-align: center; font-family: var(--display); font-weight: 600; font-size: 38px; color: var(--paper); letter-spacing: 0.5px; line-height: 1; }

  .declaration { position: absolute; left: 565px; top: 18px; width: 208px; font-size: 10px; line-height: 1.22; }
  .declaration p { margin-bottom: 9px; }
  .declaration strong { font-weight: 700; }
  .nutrition { width: 100%; border-collapse: collapse; font-size: 7px; margin: 4px 0 12px; }
  .nutrition th, .nutrition td { border: 0.8px solid var(--ink); padding: 1px 2px; text-align: left; }
  .nutrition th { font-weight: 700; }
  .nutrition td:last-child, .nutrition th:last-child { text-align: right; }
  .nutrition .sub td:first-child { font-weight: 400; }
  .nutrition tr:not(.sub) td:first-child { font-weight: 700; }
  .maker { font-size: 10px; line-height: 1.2; }
  .maker strong { display: block; font-size: 10.5px; }
</style>
</head>
<body>
<main class="canvas">

  <section class="lid-tag" aria-label="Deckeletikett">
    <div class="lid-tag__disc"></div>
    <div class="lid-tag__strip"></div>
    <div class="brand-name">TOPF<br>ZAUBER</div>
    <span class="lid-tag__claim">FRISCH ZUBEREITET</span>
  </section>

  <section class="jar-label jar-label--tomato" aria-label="Etikett Tomatensauce">
    <div class="barcode-space"></div>
    <div class="rule-vertical rule-vertical--left"></div>
    <div class="best-before"><strong>Mindestens<br>haltbar bis:</strong>Siehe Deckel</div>
    <div class="rule-short"></div>
    <div class="net-weight">360g</div>

    <div class="herb-illustration" role="img" aria-label="Illustration von Kräutern und Blättern rund um das Logo"></div>
    <div class="brand-disc"><div class="brand-name">TOPF<br>ZAUBER</div></div>
    <div class="diet-stamp" role="img" aria-label="Stempel vegetarisch, glutenfrei"></div>
    <div class="product-name">TOMATENSAUCE</div>

    <div class="rule-vertical rule-vertical--right"></div>
    <div class="declaration">
      <p><strong>Zutaten:</strong> Lorem ipsum dolor sit amet, consectetuer adipiscing elit, sed diam nonummy nibh euismod est.</p>
      <p><strong>Hinweise:</strong> Kann Spuren von Sellerie und Nüssen enthalten.</p>
      <p><strong>Lagerung:</strong> Kühl, trocken und lichtge­schützt lagern. Nach dem Öffnen im Kühlschrank aufbewahren und innerhalb weniger Tage aufbrauchen.</p>
      <table class="nutrition">
        <tr><th>Nährwerte</th><th>per 100 g</th></tr>
        <tr><td>Brennwert</td><td>1298 kJ / 310 kcal</td></tr>
        <tr><td>Fett</td><td>0,8 g</td></tr>
        <tr class="sub"><td>Davon gesättigte Fettsäuren</td><td>&lt;0,1 g</td></tr>
        <tr><td>Kohlenhydrate</td><td>5,4 g</td></tr>
        <tr class="sub"><td>Davon Zucker</td><td>6,3 g</td></tr>
        <tr><td>Protein</td><td>2,7 g</td></tr>
        <tr><td>Salz</td><td>0,53 g</td></tr>
      </table>
      <div class="maker"><strong>Hersteller und Vertrieb:</strong>Partyservice Wendlinger, Matthias Wendlinger<br>Lindauer Gasse 7, D-88512 Ostrach<br><strong>www.topfzauber-beispiel.de</strong></div>
    </div>
  </section>

  <section class="jar-label jar-label--bolognese" aria-label="Etikett Bolognese">
    <div class="barcode-space"></div>
    <div class="rule-vertical rule-vertical--left"></div>
    <div class="best-before"><strong>Mindestens<br>haltbar bis:</strong>Siehe Deckel</div>
    <div class="rule-short"></div>
    <div class="net-weight">360g</div>

    <div class="herb-illustration" role="img" aria-label="Illustration von Kräutern und Blättern rund um das Logo"></div>
    <div class="brand-disc"><div class="brand-name">TOPF<br>ZAUBER</div></div>
    <div class="diet-stamp" role="img" aria-label="Stempel laktosefrei"></div>
    <div class="product-name">BOLOGNESE</div>

    <div class="rule-vertical rule-vertical--right"></div>
    <div class="declaration">
      <p><strong>Zutaten:</strong> Lorem ipsum dolor sit amet, consectetuer adipiscing elit, sed diam nonummy nibh euismod est.</p>
      <p><strong>Hinweise:</strong> Kann Spuren von Sellerie und Nüssen enthalten.</p>
      <p><strong>Lagerung:</strong> Kühl, trocken und lichtge­schützt lagern. Nach dem Öffnen im Kühlschrank aufbewahren und innerhalb weniger Tage aufbrauchen.</p>
      <table class="nutrition">
        <tr><th>Nährwerte</th><th>per 100 g</th></tr>
        <tr><td>Brennwert</td><td>1298 kJ / 310 kcal</td></tr>
        <tr><td>Fett</td><td>0,8 g</td></tr>
        <tr class="sub"><td>Davon gesättigte Fettsäuren</td><td>&lt;0,1 g</td></tr>
        <tr><td>Kohlenhydrate</td><td>5,4 g</td></tr>
        <tr class="sub"><td>Davon Zucker</td><td>6,3 g</td></tr>
        <tr><td>Protein</td><td>2,7 g</td></tr>
        <tr><td>Salz</td><td>0,53 g</td></tr>
      </table>
      <div class="maker"><strong>Hersteller und Vertrieb:</strong>Partyservice Wendlinger, Matthias Wendlinger<br>Lindauer Gasse 7, D-88512 Ostrach<br><strong>www.topfzauber-beispiel.de</strong></div>
    </div>
  </section>

</main>
</body>
</html>
```